Business Card Design

I am a new realtor. To stand out from the other 25 realtors in my firm I need a card that will stand out. I am the youngest realtor here, so I want something to reflect that. Something different, as opposed to the same old traditional, boring cards everyone else has. It of course needs to have my picture which I will download for you ( I included a black and white option as well as color. Either are fine) and you can crop it or do whatever you need to make it look the best. Our company colors are red and white. These don't have to be the only colors on the card, but the red especially needs to be a focal color. I like a clean, stream-line look while still eye-catching. Not over the top busy.
While I do have to provide the company logo, I am a contractor. Therefore, I want the focus on me and my information.
Industry/Entity Type
Realtor
Contact Information for Business Card
Marissa Dunholt
Realtor (this needs the realtor logo which has the R in the circle at the end)
(office)555.318.4620
(cell) 555.742.9037
Mdunholt@brv-homesale.example
It will also need our company logo which I will download and send
Requirements
Nice to have
- I like the look of the foil or metallic. However, this is definitely not a requirement

```html
<!DOCTYPE html>
<html lang="en">
<head>
<meta charset="utf-8">
<title>Marissa Dunholt – Realtor Business Card</title>
<link href="https://fonts.googleapis.com/css2?family=Parisienne&family=Josefin+Sans:wght@300;400&display=swap" rel="stylesheet">
<style>
  :root {
    --page-bg: #d9d9d9;
    --front-black: #0b0b0b;
    --pattern-dark: #1a1a1a;
    --pattern-mid: #262626;
    --silver-light: #f2f2f2;
    --silver-dark: #9a9a9a;
    --slate: #2b343a;
    --slate-deep: #1f262b;
    --photo-light: #f4f4f4;
    --photo-warm: #c9b4a3;
    --name-blue: #8cc4d8;
    --text-light: #c8d3d8;
    --text-muted: #8e999f;
    --brand-red: #e8363b;
  }
  html, body {
    margin: 0;
    width: 1200px;
    height: 900px;
    overflow: hidden;
    background: var(--page-bg);
  }
  .canvas { position: relative; width: 1200px; height: 900px; }
  .card {
    position: absolute;
    left: 250px;
    width: 700px;
    height: 400px;
    overflow: hidden;
    box-shadow: 0 6px 18px rgba(0,0,0,0.25);
  }

  /* Front */
  .card-front { top: 35px; background: var(--front-black); }
  .pattern-band {
    position: absolute;
    left: 0;
    width: 100%;
    height: 105px;
    background: linear-gradient(180deg, var(--pattern-mid), var(--pattern-dark));
  }
  .pattern-band.top { top: 0; }
  .pattern-band.bottom { bottom: 0; background: linear-gradient(0deg, var(--pattern-mid), var(--pattern-dark)); }
  .front-name {
    position: absolute;
    top: 132px;
    left: 0;
    width: 100%;
    text-align: center;
    white-space: nowrap;
    font-family: "Parisienne", cursive;
    font-size: 70px;
    line-height: 1;
    color: var(--silver-light);
    background: linear-gradient(180deg, var(--silver-light), var(--silver-dark));
    -webkit-background-clip: text;
    background-clip: text;
    -webkit-text-fill-color: transparent;
  }
  .front-title {
    position: absolute;
    top: 206px;
    left: 0;
    width: 100%;
    box-sizing: border-box;
    padding-left: 110px;
    text-align: center;
    white-space: nowrap;
    font-family: "Parisienne", cursive;
    font-size: 30px;
    line-height: 1;
    color: var(--silver-dark);
  }
  .front-title sup { font-family: "Josefin Sans", sans-serif; font-size: 12px; }

  /* Back */
  .card-back {
    top: 465px;
    background: radial-gradient(circle at 70% 40%, var(--slate), var(--slate-deep));
  }
  .portrait {
    position: absolute;
    left: 0;
    top: 0;
    width: 290px;
    height: 400px;
    background: linear-gradient(160deg, var(--photo-light) 0%, var(--photo-light) 45%, var(--photo-warm) 100%);
  }
  .brand-mark {
    position: absolute;
    top: 42px;
    right: 32px;
    display: flex;
    align-items: center;
    gap: 10px;
    white-space: nowrap;
    font-family: "Josefin Sans", sans-serif;
    font-weight: 400;
    font-size: 19px;
    letter-spacing: 2px;
    color: var(--brand-red);
  }
  .brand-square { width: 16px; height: 16px; background: var(--brand-red); flex: none; }
  .contact {
    position: absolute;
    left: 318px;
    top: 148px;
    width: 355px;
    font-family: "Josefin Sans", sans-serif;
    font-weight: 300;
    white-space: nowrap;
  }
  .contact-name {
    font-size: 25px;
    letter-spacing: 3px;
    color: var(--name-blue);
    text-transform: uppercase;
    line-height: 1;
  }
  .contact-role {
    font-size: 14px;
    letter-spacing: 5px;
    color: var(--text-light);
    margin-top: 6px;
  }
  .dotted-rule { border-top: 2px dotted var(--text-muted); margin: 10px 0; }
  .contact-row {
    display: flex;
    align-items: center;
    gap: 8px;
    font-size: 17px;
    letter-spacing: 1px;
    color: var(--text-light);
    height: 28px;
  }
  .contact-row svg { width: 22px; height: 20px; flex: none; }
  .contact-address {
    font-size: 16px;
    letter-spacing: 0.5px;
    color: var(--text-muted);
  }
</style>
</head>
<body>
<div class="canvas">

  <section class="card card-front">
    <div class="pattern-band top" role="img" aria-label="Dark damask ornament band"></div>
    <div class="pattern-band bottom" role="img" aria-label="Dark damask ornament band"></div>
    <div class="front-name">Marissa Dunholt</div>
    <div class="front-title">Realtor<sup>®</sup></div>
  </section>

  <section class="card card-back">
    <div class="portrait" role="img" aria-label="Portrait photo of the realtor in a white shirt with a beaded necklace"></div>

    <div class="brand-mark"><span class="brand-square"></span><span>HALVERN REED REALTY</span></div>

    <div class="contact">
      <div class="contact-name">Marissa Dunholt</div>
      <div class="contact-role">REALTOR</div>
      <div class="dotted-rule"></div>
      <div class="contact-row">
        <svg viewBox="0 0 22 20" aria-hidden="true"><rect x="3" y="7" width="16" height="11" rx="2" fill="none" stroke="#8cc4d8" stroke-width="1.5"/><path d="M2 7 Q11 0 20 7" fill="none" stroke="#8cc4d8" stroke-width="2"/><circle cx="11" cy="12.5" r="2.5" fill="none" stroke="#8cc4d8" stroke-width="1.3"/></svg>
        <span>: 555.318.4620</span>
      </div>
      <div class="contact-row">
        <svg viewBox="0 0 22 20" aria-hidden="true"><rect x="7" y="1" width="9" height="18" rx="1.5" fill="none" stroke="#8cc4d8" stroke-width="1.5"/><rect x="9" y="4" width="5" height="6" fill="#8cc4d8"/></svg>
        <span>: 555.742.9037</span>
      </div>
      <div class="contact-row">
        <svg viewBox="0 0 22 20" aria-hidden="true"><rect x="2" y="4" width="18" height="12" fill="none" stroke="#8cc4d8" stroke-width="1.5"/><path d="M2 4 L11 11 L20 4" fill="none" stroke="#8cc4d8" stroke-width="1.5"/></svg>
        <span>: Mdunholt@brv-homesale.example</span>
      </div>
      <div class="dotted-rule"></div>
      <div class="contact-address">4820 Larkmoor Ave, Fenwick, OK 74990</div>
    </div>
  </section>

</div>
</body>
</html>
```